Outdoor Company Business Card design

We are an outdoor adventure company needing a business card. We sell outdoor adventures and clothing. Please use our logo in the business card. We are looking for something unique but delivers a clear message as to who we are. Please be creative

Target Market(s)

Outdoor adventures

Industry/Entity Type

Business

Contact Information for Business Card

Business name: TrailBirch If using the logo, no need to have a spot for the name
Owner / CEO: Ross Dalby
Website: TrailBirch.example
Facebook: Facebook.com/TrailBirch
Instagram: @dalby_ross
phone number: 555-304-7192
Email: Dalbycrew@TrailBirch.example

Colors

Designer to choose colors to be used in the design.

Requirements
Must have
• The business card must include the details mentioned above. ie logo, my name, email, facebook, instagram, website, and phone number.
Should not have
• should not be cluttered or look messy

```html
<!DOCTYPE html>
<html lang="en">
<head>
<meta charset="utf-8">
<title>TrailBirch Business Card</title>
<link rel="stylesheet" href="https://fonts.googleapis.com/css2?family=Montserrat:wght@600&family=Roboto:wght@400&family=Roboto+Condensed:wght@700&display=swap">
<style>
  :root {
    --backdrop: #2b2b2b;
    --paper: #f1f1f1;
    --brand-blue: #1273bd;
    --brand-orange: #f15a29;
    --ink: #4a4a4a;
    --white: #ffffff;
  }
  * { margin: 0; padding: 0; box-sizing: border-box; }
  html, body { width: 1200px; height: 960px; overflow: hidden; }
  body { background: var(--backdrop); position: relative; }

  .card {
    position: absolute;
    width: 600px;
    height: 342px;
    border-radius: 18px;
    overflow: hidden;
  }
  .card-front { left: 314px; top: 113px; background: var(--paper); }
  .card-back { left: 311px; top: 472px; background: var(--brand-orange); }

  .front-stripes { position: absolute; inset: 0; }

  .social-links { position: absolute; top: 22px; right: 26px; display: flex; gap: 10px; }
  .social-box { width: 22px; height: 22px; background: var(--white); border-radius: 4px; }

  .brand-name {
    position: absolute;
    left: 43px;
    top: 94px;
    font-family: "Montserrat", sans-serif;
    font-weight: 600;
    font-size: 34px;
    letter-spacing: 0.5px;
    color: var(--brand-blue);
  }

  .person { position: absolute; left: 43px; top: 194px; }
  .person-name {
    font-family: "Roboto Condensed", sans-serif;
    font-weight: 700;
    font-size: 22px;
    color: var(--brand-blue);
    line-height: 1;
  }
  .person-title {
    font-family: "Roboto Condensed", sans-serif;
    font-weight: 700;
    font-size: 15px;
    color: var(--brand-orange);
    margin-top: 3px;
  }

  .contact-list { position: absolute; left: 43px; top: 246px; list-style: none; }
  .contact-item {
    display: flex;
    align-items: center;
    gap: 8px;
    height: 19px;
    font-family: "Roboto", sans-serif;
    font-size: 14px;
    color: var(--ink);
  }
  .contact-icon { width: 13px; height: 13px; flex: none; }

  .back-brand {
    position: absolute;
    top: 40px;
    width: 100%;
    text-align: center;
    font-family: "Montserrat", sans-serif;
    font-weight: 600;
    font-size: 44px;
    color: var(--white);
    letter-spacing: 1px;
    line-height: 1;
  }
  .back-url {
    position: absolute;
    top: 94px;
    width: 100%;
    text-align: center;
    font-family: "Roboto", sans-serif;
    font-size: 14px;
    letter-spacing: 5px;
    color: var(--white);
  }
  .back-artwork {
    position: absolute;
    left: 0;
    bottom: 0;
    width: 100%;
    height: 212px;
    background: linear-gradient(to bottom, var(--white) 0%, #d7e6f2 40%, var(--brand-blue) 100%);
  }
</style>
</head>
<body>

  <section class="card card-front">
    <svg class="front-stripes" width="600" height="342" viewBox="0 0 600 342" aria-hidden="true">
      <polygon points="364,0 372,0 538,342 530,342" fill="var(--brand-blue)"/>
      <polygon points="376,0 600,0 600,342 542,342" fill="var(--brand-orange)"/>
    </svg>

    <div class="social-links" aria-hidden="true">
      <span class="social-box"></span>
      <span class="social-box"></span>
    </div>

    <div class="brand-name">TRAILBIRCH</div>

    <div class="person">
      <div class="person-name">ROSS DALBY</div>
      <div class="person-title">OWNER / CEO</div>
    </div>

    <ul class="contact-list">
      <li class="contact-item">
        <svg class="contact-icon" viewBox="0 0 16 16" aria-hidden="true">
          <path d="M3.5 1 L6 1 L7 5 L5.3 6.3 C6.2 8.2 7.8 9.8 9.7 10.7 L11 9 L15 10 L15 12.5 C15 14 14 15 12.5 15 C6.5 15 1 9.5 1 3.5 C1 2 2 1 3.5 1 Z" fill="var(--brand-blue)"/>
        </svg>
        555-304-7192
      </li>
      <li class="contact-item">
        <svg class="contact-icon" viewBox="0 0 16 16" aria-hidden="true">
          <rect x="1" y="3" width="14" height="10" fill="var(--brand-blue)"/>
          <polyline points="1,3 8,9 15,3" fill="none" stroke="var(--paper)" stroke-width="1.4"/>
        </svg>
        Dalbycrew@TrailBirch.example
      </li>
      <li class="contact-item">
        <svg class="contact-icon" viewBox="0 0 16 16" aria-hidden="true">
          <circle cx="8" cy="8" r="7" fill="var(--brand-blue)"/>
          <ellipse cx="8" cy="8" rx="3" ry="7" fill="none" stroke="var(--paper)" stroke-width="1"/>
          <line x1="1" y1="8" x2="15" y2="8" stroke="var(--paper)" stroke-width="1"/>
        </svg>
        www.TrailBirch.example
      </li>
    </ul>
  </section>

  <section class="card card-back">
    <div class="back-brand">TRAILBIRCH</div>
    <div class="back-url">WWW.TRAILBIRCH.EXAMPLE</div>
    <div class="back-artwork" role="img" aria-label="Large white and blue illustration of mountain peaks over rushing water"></div>
  </section>

</body>
</html>
```